FlockVault.net website design

We are looking for a design for a new website we are about to launch called FlockVault.net. FlockVault.net is an online discount wine site that will focus on selling only one wine at a time. (This potentially may become two or three wines at a time in the future but only one for now). The wine that is up for sale will not actually be sold until a pre-set number of buyers “the group” commits to buying the wine. If the threshold of buyers is not met then the wine is not sold. This group aspect is what makes the site unique. By only selling the wine when the group commits to buying it we are able to deliver them a great wine at a fantastic price.
The website should convey a fun feeling while also indicating that this is a place where serious wine enthusiasts can shop. We will be providing information, ratings, and reviews about the wines that are currently on sale.
Updates
Target Market(s)
The target market is a wide range of wine enthusiasts, from people in their 20s and 30s to more mature and serious wine connoisseurs.
Industry/Entity Type
Shop
Requirements
Must have
- Below is a list of specifications for the website:
1) Main page with our logo (which includes green, purple, and a magenta wine color) that showcases the current wine that's for sale
- The site’s main focus should be on selling ONE bottle of wine at a time at group rate.
- The site should capture the group buying concept as this is what differentiates our site from the others. Visitors to the site should get the sense that they are part of a special community that is getting a great deal because they are buying the wine as a group.
- A meter or better yet an animation should be used to indicate if the tipping point has been met for a sale. We’d like to see some creative ideas here.
- Nice high-res photo of the wine bottle
- Detailed description of what kind of wine it is, where the wine is from, type of grape, vino observer and other ratings, description of what it tastes like. We would like the option to provide as much detail here as possible.
- Breakdown on what the prices are per bottle and the discount we're giving. We would like to show the original price as compared to the FlockVault.net price.
- Potentially show a list of upcoming wines. Maybe not the exact wine that will be for sale next but some info to entice users to keep checking.
2) User Account Log in
- Ability to create and log into a personal account
The personal account should be able to:
-store users' credit card and shipping information as well as past orders
-allow you to opt in or out of flock vault emails
-potentially store wine preference or ratings information
-refer a friend option where you get some kind of incentive
3) The Group Concept. The website design must include a few aspects that identify FlockVault.net as a social site, not simply a wine sale site.
- Some kind of indicator showing if the group threshold has been met or not. We would like to see some type of animation with wine bottles filling up, or grapes on a scale-something that would change as the number of people buying into the sale increase.
- Button to join the group purchase
4) General Site Content must include:
- Email link to send questions to support
- Information on how shipping works and other FAQs
- Legal disclaimer
- Links to FriendPage and Chirper
Nice to have
- It would be nice to have a discussion board where FlockVault members can discuss wines.
Should not have
- The design should not be for a general wine store that sells a variety of different wines.

```html
<!DOCTYPE html>
<html lang="en">
<head>
<meta charset="utf-8">
<title>FlockVault.net – Current Group Wine</title>
<link href="https://fonts.googleapis.com/css2?family=Arimo:wght@400;700&family=Questrial&display=swap" rel="stylesheet">
<style>
:root{
  --magenta:#a5164f;
  --magenta-soft:#c2306a;
  --green:#7cb51f;
  --green-dark:#5f9412;
  --purple:#6a2a8c;
  --cream:#fbf4dc;
  --gold:#d9b43a;
  --ink:#2b2b2b;
  --muted:#6b6b6b;
  --white:#ffffff;
}
*{box-sizing:border-box;margin:0;padding:0}
html,body{width:1200px;height:1146px;overflow:hidden}
body{font-family:"Arimo",Arial,sans-serif;color:var(--ink);background:var(--white);position:relative}
a{color:inherit}

.topbar{position:absolute;left:0;top:0;width:1200px;height:89px;background:var(--magenta)}
.main-nav{position:absolute;left:150px;top:0;height:89px;display:flex;align-items:center}
.main-nav a{color:var(--white);font-size:13px;text-transform:uppercase;text-decoration:underline;width:105px;text-align:center;position:relative}
.main-nav a.current{color:#f3b6cc}
.main-nav a+a::before{content:"";position:absolute;left:-8px;top:-26px;width:1px;height:56px;background:rgba(255,255,255,.55);transform:skewX(-22deg)}
.account-links{position:absolute;right:117px;top:20px;text-align:right;font-size:11px;line-height:18px;color:#f0c2d3}
.account-links strong{color:var(--white);font-weight:400}

.brandbar{position:absolute;left:0;top:89px;width:1200px;height:95px;background:var(--cream)}
.brand{position:absolute;left:125px;top:14px;display:flex;align-items:center;gap:14px}
.brand-mark{width:50px;height:50px;border-radius:50%;background:var(--purple)}
.brand-name{font-size:38px;font-weight:700;color:var(--magenta);line-height:1}
.brand-line{position:absolute;left:206px;top:66px;white-space:nowrap;font-size:11px;color:var(--muted)}
.social-box{position:absolute;left:778px;top:27px;width:278px;height:43px;background:var(--white);border-radius:8px;box-shadow:0 1px 4px rgba(0,0,0,.15);display:flex;align-items:center;padding:0 10px;gap:6px;font-size:8px;text-transform:uppercase;color:var(--muted);white-space:nowrap}
.social-box .label{margin-right:4px}
.net{display:inline-block;padding:4px 4px;border-radius:4px;background:#eef3f6;color:var(--ink);font-size:8px;text-transform:uppercase;white-space:nowrap}

.product{position:absolute;left:0;top:184px;width:1200px;height:316px}
.bottle-photo{position:absolute;left:145px;top:13px;width:184px;height:253px;border-radius:6px;background:linear-gradient(90deg,#2a1a22 0 22%,#fff 22% 30%,#d9b678 30% 70%,#fff 70% 78%,#3a4a1e 78%)}
.wine-title{position:absolute;left:374px;top:28px;font-size:15px;font-weight:700;color:var(--green);text-transform:uppercase;letter-spacing:.2px}
.facts{position:absolute;left:374px;top:84px;width:370px;font-size:12px;text-transform:uppercase;line-height:18px}
.origin{font-size:10.5px;margin-bottom:14px;white-space:nowrap}
.ratings{display:grid;grid-template-columns:72px auto}
.ratings span:first-child{font-weight:700}
.specs{margin-top:16px;display:grid;grid-template-columns:72px auto}
.spec-table{position:absolute;left:771px;top:83px;display:grid;grid-template-columns:144px 140px;font-size:11px;line-height:18px;text-transform:uppercase}
.spec-table b{font-size:12px}
.price-box{position:absolute;left:765px;top:146px;width:289px;height:141px;background:var(--cream);border-radius:4px;padding:6px 7px}
.price-row{display:flex;justify-content:space-between;font-size:15px;font-weight:700;text-transform:uppercase;padding:0 2px;line-height:18px}
.price-row.group{color:var(--green)}
.btn{display:flex;align-items:center;justify-content:center;height:40px;border-radius:5px;color:var(--white);font-size:13px;font-weight:700;text-transform:uppercase;text-decoration:none;text-shadow:0 1px 1px rgba(0,0,0,.25)}
.btn-join{margin-top:10px;background:linear-gradient(#96cf35,var(--green-dark));border:1px solid var(--green-dark)}
.btn-discuss{margin-top:6px;background:linear-gradient(#ecd062,var(--gold));border:1px solid #c69d22}

.group-band{position:absolute;left:0;top:500px;width:1200px;height:178px;background:var(--cream)}
.bump{position:absolute;top:90px;width:240px;height:128px;border-radius:50%;background:var(--cream)}
.group-heading{position:absolute;left:0;top:14px;width:1200px;text-align:center;font-family:"Questrial",Arial,sans-serif;font-size:24px;font-weight:400;letter-spacing:4px;color:var(--green)}
.group-heading em{font-style:normal;color:var(--magenta)}
.stat{position:absolute;top:60px;width:200px;text-align:center}
.stat svg{display:block;margin:0 auto}
.stat .caption{margin-top:22px;font-size:12px;color:var(--ink)}
.big-pct{height:94px;display:flex;align-items:center;justify-content:center;font-size:50px;font-weight:700;color:var(--magenta)}
.big-pct small{font-size:24px}

.writeup{position:absolute;left:137px;top:733px;width:926px;height:320px;border:1px solid #d8d2b8;border-radius:6px;background:linear-gradient(#fbfaf3,#d4cfb6);overflow:hidden}
.writeup-head{height:39px;border-bottom:1px solid #ddd7bf;background:linear-gradient(#fffef8,#f0ecd9);padding:9px 12px}
.writeup-head a{font-size:14px;color:var(--magenta)}
.writeup-body{padding:10px 10px;font-size:11.3px;line-height:17.6px;color:#3a3a3a}
.writeup-body p+p{margin-top:17px}
.writeup-photo{float:right;width:90px;height:89px;margin:0 0 6px 18px;border-radius:4px;background:linear-gradient(135deg,#3a2030,#b48a6a 55%,#e9d8b8)}
.read-more{position:absolute;right:12px;bottom:6px;font-size:9px;color:var(--ink);text-decoration:none}

.footer{position:absolute;left:0;top:1083px;width:1200px;height:63px;background:var(--cream)}
.footer-links{position:absolute;left:122px;top:14px;font-size:11px;text-transform:uppercase;color:var(--ink)}
.copyright{position:absolute;left:122px;top:40px;font-size:10px;color:var(--ink)}
.follow{position:absolute;left:986px;top:12px;font-size:11px;text-transform:uppercase}
.follow-nets{display:flex;gap:4px;margin-top:7px}
</style>
</head>
<body>

<header class="topbar">
  <nav class="main-nav">
    <a class="current" href="#">Home</a>
    <a href="#">About</a>
    <a href="#">Wines</a>
    <a href="#">Support</a>
    <a href="#">FAQs</a>
    <a href="#">Help</a>
    <a href="#">Contact</a>
  </nav>
  <div class="account-links">
    <div><strong>Welcome!</strong> Login or Sign Up</div>
    <div>Order Status &amp; Help</div>
    <div>My Account &nbsp;/&nbsp; View Cart</div>
  </div>
</header>

<section class="brandbar">
  <div class="brand">
    <span class="brand-mark"></span>
    <span class="brand-name">FlockVault</span>
  </div>
  <span class="brand-line">One great bottle, bought together</span>
  <div class="social-box">
    <span class="label">Social Networks</span>
    <span class="net">Chirper</span>
    <span class="net">FriendPage</span>
    <span class="net">CirclePlus</span>
  </div>
</section>

<section class="product">
  <div class="bottle-photo" role="img" aria-label="Three wine bottles beside an open wooden gift box"></div>
  <h1 class="wine-title">Halloway Vineyard Estate Grown Napa Valley Cabernet Sauvignon 2007</h1>
  <div class="facts">
    <p class="origin">From the "extraordinary" California North Coast region</p>
    <div class="ratings">
      <span>Ratings:</span>
      <span>90 Rating - Grape Devotee!<br>92 Score - Vino Observer!<br>93 Rating - Roland Parrish!<br>Online Exclusive! - Grape Devotee!</span>
    </div>
    <div class="specs">
      <b>Unit Size</b><span>750.00 ML</span>
      <b>Varietal:</b><span>Cabernet Sauvignon</span>
      <b>Vintage:</b><span>2007</span>
    </div>
  </div>
  <div class="spec-table">
    <b>Grape:</b><span>Cabernet Sauvignon</span>
    <b>Country:</b><span>United States</span>
    <b>Alcohol Content:</b><span>14.80 %</span>
  </div>
  <div class="price-box">
    <div class="price-row"><span>Avg. Price:</span><span>$85.00</span></div>
    <div class="price-row group"><span>Group Price:</span><span>$56.99</span></div>
    <a class="btn btn-join" href="#">Join the Group Purchase</a>
    <a class="btn btn-discuss" href="#">Discuss this Wine with Group</a>
  </div>
</section>

<section class="group-band">
  <span class="bump" style="left:155px"></span>
  <span class="bump" style="left:483px"></span>
  <span class="bump" style="left:825px"></span>
  <h2 class="group-heading">Sign Up And Join The Group For <em>Get Such A Great Deal</em></h2>

  <div class="stat" style="left:175px">
    <svg width="94" height="94" viewBox="0 0 94 94" aria-hidden="true">
      <circle cx="47" cy="47" r="40" fill="none" stroke="#e7dfc6" stroke-width="12" stroke-dasharray="2 3"/>
      <circle cx="47" cy="47" r="40" fill="none" stroke="var(--magenta-soft)" stroke-width="12" stroke-dasharray="2 3" transform="rotate(-90 47 47)"/>
      <circle cx="47" cy="47" r="40" fill="none" stroke="var(--cream)" stroke-width="14" stroke-dasharray="0 206 45 0" transform="rotate(-90 47 47)"/>
      <text x="47" y="53" text-anchor="middle" font-family="Arimo,Arial,sans-serif" font-size="19" font-weight="700" fill="var(--magenta)">82<tspan font-size="11">%</tspan></text>
    </svg>
    <p class="caption">People Are Signed Up.</p>
  </div>

  <div class="stat" style="left:503px">
    <div class="big-pct">85<small>%</small></div>
    <p class="caption">* required.</p>
  </div>

  <div class="stat" style="left:845px">
    <svg width="94" height="94" viewBox="0 0 94 94" aria-hidden="true">
      <circle cx="47" cy="47" r="40" fill="none" stroke="#efe6cf" stroke-width="12"/>
      <circle cx="47" cy="47" r="40" fill="none" stroke="var(--magenta-soft)" stroke-width="12" stroke-dasharray="221 30" transform="rotate(-90 47 47)"/>
      <text x="47" y="53" text-anchor="middle" font-family="Arimo,Arial,sans-serif" font-size="19" font-weight="700" fill="var(--magenta)">88<tspan font-size="11">%</tspan></text>
    </svg>
    <p class="caption">People Are Online.</p>
  </div>
</section>

<article class="writeup">
  <div class="writeup-head"><a href="#">write-up</a></div>
  <div class="writeup-body">
    <div class="writeup-photo" role="img" aria-label="Row of wine bottles on a cellar shelf"></div>
    <p>"At vero eos et accusamus et iusto odio dignissimos ducimus qui blanditiis praesentium voluptatum deleniti atque corrupti quos dolores et quas molestias excepturi sint occaecati cupiditate non provident, similique sunt in culpa qui officia deserunt mollitia animi, id est laborum et dolorum fuga. Et harum quidem rerum facilis est et expedita distinctio. Nam libero tempore, cum soluta nobis est eligendi optio cumque nihil impedit quo minus id quod maxime placeat facere possimus, omnis voluptas assumenda est, omnis dolor repellendus. Temporibus autem quibusdam et aut officiis debitis aut rerum necessitatibus saepe eveniet ut et voluptates repudiandae sint et molestiae non recusandae. Itaque earum rerum hic tenetur a sapiente delectus, ut aut reiciendis voluptatibus maiores alias consequatur aut perferendis doloribus asperiores repellat."</p>
    <p>"At vero eos et accusamus et iusto odio dignissimos ducimus qui blanditiis praesentium voluptatum deleniti atque corrupti quos dolores et quas molestias excepturi sint occaecati cupiditate non provident, similique sunt in culpa qui officia deserunt mollitia animi, id est laborum et dolorum fuga. Et harum quidem rerum facilis est et expedita distinctio. Nam libero tempore, cum soluta nobis est eligendi optio cumque nihil impedit quo minus id quod maxime placeat facere possimus, omnis voluptas assumenda est, omnis dolor repellendus. Temporibus autem quibusdam et aut officiis debitis aut rerum necessitatibus saepe eveniet ut et voluptates repudiandae sint et molestiae non recusandae. Itaque earum rerum hic tenetur a sapiente delectus, ut aut reiciendis voluptatibus maiores alias consequatur aut perferendis doloribus asperiores repellat."</p>
  </div>
  <a class="read-more" href="#">Read more &gt;&gt;</a>
</article>

<footer class="footer">
  <nav class="footer-links">Home ~ About ~ Still have a question ? ~ How shipping works ? ~ FAQs ~ Disclaimer ~ Help ~ Contact</nav>
  <p class="copyright">© 2011 flockvault.net. All rights reserved.</p>
  <div class="follow">
    Follow us:
    <div class="follow-nets">
      <span class="net">Chirper</span>
      <span class="net">FriendPage</span>
      <span class="net">CirclePlus</span>
    </div>
  </div>
</footer>

</body>
</html>
```